Brivora Australia Company Values.

We have just completed our company purpose, beliefs and values (for the first time, we have not had these before)
We are now wanting to add images to each company value as a visual
so they are easily identified and understood for all our staff - we need them to remember the 5 Values.
We are a manufacturer of dental materials and infection control products, based in Melbourne.

What we would like:
- A Poster (that can be placed in our staff lunch rooms)
- The values to be lined up Horizontally
- Image on the top of the words
- Wording does not all need to be the same text font
- No image photographs - please use image graphics
- No images with people
- No dental related graphics

Target audience: Brivora staff

Our Values are:
Think Big
Have a go, learn and adapt
If you're gonna do it, do it bloody well
Empower Others
Be a good human

I have uploaded some examples.

Target Market(s)

Brivora Team members

Industry/Entity Type

Healthcare

Colors

Designer to choose colors to be used in the design.

Requirements
Must have
• Clear horizontal layout, space between each value
Should not have
• No images with humans or dental

```html
<!DOCTYPE html>
<html lang="en">
<head>
<meta charset="utf-8">
<title>Brivora Australia – Core Values</title>
<link href="https://fonts.googleapis.com/css2?family=Allura&family=Bebas+Neue&family=Montserrat:wght@500;700&display=swap" rel="stylesheet">
<style>
  :root {
    --page: #f2f2f0;
    --blue: #0f50a6;
    --blue-band: #0d4b9d;
    --blue-skyline: #0b448f;
    --icon-block: #2c68b8;
    --white: #ffffff;
    --silver: #a9abae;
    --light: #dfe3ea;
    --divider: rgba(255,255,255,0.75);
  }
  html, body {
    margin: 0;
    width: 1200px;
    height: 900px;
    overflow: hidden;
    background: var(--page);
  }
  .poster {
    position: absolute;
    left: 20px;
    top: 49px;
    width: 1160px;
    height: 802px;
    background: var(--blue);
    overflow: hidden;
    font-family: "Montserrat", sans-serif;
    color: var(--white);
  }
  .poster > * { position: absolute; margin: 0; }

  .band {
    left: 0; top: 288px; width: 1160px; height: 239px;
    background: var(--blue-band);
    border-top: 2px dotted var(--divider);
    border-bottom: 2px dotted var(--divider);
    box-sizing: border-box;
  }
  .rule-v { width: 0; border-left: 2px dotted var(--divider); }
  .rule-band-left  { left: 276px; top: 288px; height: 239px; }
  .rule-band-right { left: 887px; top: 288px; height: 239px; }
  .rule-low-left   { left: 456px; top: 527px; height: 275px; }
  .rule-low-right  { left: 734px; top: 527px; height: 275px; }

  .skyline { background: var(--blue-skyline); opacity: .8; }
  .skyline-harbour { left: 0; top: 380px; width: 330px; height: 140px; border-radius: 60% 40% 0 0 / 70% 50% 0 0; }
  .skyline-city    { left: 790px; top: 300px; width: 370px; height: 212px; }

  .icon { background: var(--icon-block); border-radius: 6px; }

  .condensed { font-family: "Bebas Neue", sans-serif; line-height: .9; letter-spacing: .01em; white-space: nowrap; }
  .script    { font-family: "Allura", cursive; line-height: 1; color: var(--silver); white-space: nowrap; }
  .centered  { text-align: center; }

  /* Think big */
  .think      { left: 64px; top: 80px; font-size: 96px; }
  .think-icon { left: 74px; top: 168px; width: 66px; height: 74px; }
  .think-big  { left: 140px; top: 150px; font-size: 110px; transform: rotate(-8deg); }

  /* Brand */
  .brand-name { left: 356px; top: 78px; width: 400px; text-align: center; font-weight: 700; font-size: 62px; letter-spacing: -.01em; }
  .brand-web  { left: 330px; top: 218px; width: 452px; text-align: center; font-weight: 500; font-size: 27px; letter-spacing: .2em; }

  /* Have a go */
  .grow-script { left: 780px; top: 60px; font-size: 66px; }
  .grow-learn  { left: 806px; top: 130px; font-size: 74px; }
  .grow-adapt  { left: 806px; top: 206px; font-size: 74px; }
  .grow-icon   { left: 980px; top: 200px; width: 72px; height: 72px; }

  /* Core values */
  .core   { left: 330px; top: 298px; width: 500px; text-align: center; font-weight: 700; font-size: 118px; letter-spacing: .04em; color: var(--silver); line-height: 1; }
  .values { left: 280px; top: 412px; width: 600px; text-align: center; font-weight: 700; font-size: 122px; letter-spacing: .04em; line-height: 1; }

  /* Do it well */
  .well-icon   { left: 211px; top: 556px; width: 58px; height: 60px; }
  .well-script { left: 28px; top: 606px; width: 410px; font-size: 54px; }
  .well-title  { left: 28px; top: 683px; width: 410px; font-size: 62px; color: var(--light); }

  /* Empower others */
  .empower-icon   { left: 572px; top: 556px; width: 46px; height: 60px; }
  .empower-script { left: 462px; top: 610px; width: 266px; font-size: 62px; }
  .empower-title  { left: 462px; top: 672px; width: 266px; font-size: 66px; }

  /* Good human */
  .human-icon   { left: 850px; top: 606px; width: 42px; height: 54px; }
  .human-be     { left: 902px; top: 612px; font-size: 72px; }
  .human-script { left: 742px; top: 660px; width: 410px; font-size: 66px; }
</style>
</head>
<body>
<main class="poster">
  <div class="band"></div>
  <div class="skyline skyline-harbour" role="img" aria-label="Silhouette of the harbour, opera house and bridge"></div>
  <div class="skyline skyline-city" role="img" aria-label="Silhouette of city skyscrapers"></div>
  <div class="rule-v rule-band-left"></div>
  <div class="rule-v rule-band-right"></div>
  <div class="rule-v rule-low-left"></div>
  <div class="rule-v rule-low-right"></div>

  <h2 class="condensed think">Think</h2>
  <div class="icon think-icon" role="img" aria-label="Icon: head with a light bulb"></div>
  <p class="script think-big">Big</p>

  <h1 class="brand-name">Brivora</h1>
  <p class="brand-web">www.brivora.com</p>

  <p class="script grow-script">Have a grow</p>
  <h2 class="condensed grow-learn">Learn and</h2>
  <h2 class="condensed grow-adapt">Adapt</h2>
  <div class="icon grow-icon" role="img" aria-label="Icon: open book with a light bulb"></div>

  <p class="core">CORE</p>
  <p class="values">VALUES</p>

  <div class="icon well-icon" role="img" aria-label="Icon: flexed arm showing strength"></div>
  <p class="script centered well-script">If you're gonna do it</p>
  <h2 class="condensed centered well-title">Do it bloody well</h2>

  <div class="icon empower-icon" role="img" aria-label="Icon: raised fist"></div>
  <p class="script centered empower-script">Empower</p>
  <h2 class="condensed centered empower-title">Others</h2>

  <div class="icon human-icon" role="img" aria-label="Icon: head with a heart"></div>
  <h2 class="condensed human-be">Be a</h2>
  <p class="script centered human-script">Good human</p>
</main>
</body>
</html>
```